Tellwick Asset Management - Corporate Letter Head Project

Looking for a classy design based on our current logo. Please find current logo source file in files. With our color scheme.

Target Market(s)

We're an investment firm, the letterhead needs to look professional and attractive to clients.

Industry/Entity Type

Hedgefund

Colors
0054AA
0677BA
7BADD7
CADEEF
E8F1F8

Requirements
Must have
• Our logo, address, phone number, and email

```html
<!DOCTYPE html>
<html lang="en">
<head>
<meta charset="utf-8">
<title>Tellwick Asset Management – Stationery</title>
<link href="https://fonts.googleapis.com/css2?family=Tinos&family=Source+Sans+3:wght@400;600&display=swap" rel="stylesheet">
<style>
  :root{
    --stage:#4b4f52;
    --navy:#154d8f;
    --bright:#0677ba;
    --sky:#7badd7;
    --envelope:#dbeefc;
    --paper:#ffffff;
    --card-cream:#f8f7f3;
    --ink:#1b1b1b;
    --ink-navy:#1d2a4a;
    --rule:#0677ba;
    --serif:'Tinos', 'Times New Roman', serif;
    --sans:'Source Sans 3', Arial, sans-serif;
  }
  *{margin:0;padding:0;box-sizing:border-box}
  html,body{width:938px;height:1200px;overflow:hidden}
  body{background:var(--stage);position:relative;font-family:var(--sans);color:var(--ink)}
  .sheet{position:absolute;box-shadow:4px 6px 14px rgba(0,0,0,.35)}

  /* brand name: one colour, one weight, plain dot beside */
  .brand{display:flex;align-items:center;gap:7px;color:#fff;font-family:var(--sans);font-weight:400;white-space:nowrap;line-height:1}
  .brand__dot{border-radius:50%;background:currentColor;flex:none}

  .network{position:absolute;top:0;bottom:0;
    background:linear-gradient(120deg,rgba(123,173,215,0) 0%,rgba(123,173,215,.35) 55%,rgba(123,173,215,.15) 100%)}

  /* letterhead */
  .letterhead{left:100px;top:79px;width:474px;height:670px;background:var(--paper);overflow:hidden}
  .letterhead__band{position:absolute;left:0;top:0;width:100%;height:66px;background:var(--navy)}
  .letterhead__band .brand{position:absolute;left:25px;top:25px;font-size:16px}
  .letterhead__band .brand__dot{width:12px;height:12px}
  .letterhead__band .network{left:318px;right:0}
  .watermark{position:absolute;left:250px;top:270px;width:224px;height:400px;
    background:linear-gradient(160deg,rgba(232,241,248,0) 0%,rgba(232,241,248,.6) 50%,rgba(232,241,248,0) 100%)}
  .recipient{position:absolute;left:56px;top:172px;font-size:6.9px;line-height:10.1px}
  .recipient__name{font-size:10px;line-height:12px;margin-bottom:5px}
  .letter-date{position:absolute;right:56px;top:172px;font-size:6.9px}
  .letter-body{position:absolute;left:56px;top:250px;width:363px;font-size:6.85px;line-height:10.15px;text-align:justify}
  .letter-body p{margin-bottom:10.2px}
  .signature-block{position:absolute;left:56px;top:510px}
  .signature{width:88px;height:18px;background:linear-gradient(90deg,#d9d3ee,#ebe7f7);border-radius:9px}
  .signature-block__name{font-size:9.6px;margin-top:8px;letter-spacing:.2px}
  .signature-block__role{font-size:6.9px;margin-top:3px}
  .letter-footer{position:absolute;left:35px;top:638px;display:flex;align-items:center;font-family:var(--serif);font-size:8.1px;color:var(--ink-navy)}
  .letter-footer__item{display:flex;align-items:center;gap:6px;padding:0 10px}
  .letter-footer__item:first-child{padding-left:0}
  .letter-footer__item + .letter-footer__item{border-left:1px solid var(--rule)}

  .icon{width:10px;height:10px;flex:none}

  /* business cards */
  .card-front{left:644px;top:499px;width:203px;height:113px;background:var(--navy);overflow:hidden}
  .card-front .network{left:120px;right:0;top:10px}
  .card-front .brand{position:absolute;left:0;right:0;top:51px;justify-content:center;font-size:11px;gap:5px}
  .card-front .brand__dot{width:8px;height:8px}

  .card-back{left:645px;top:637px;width:203px;height:113px;background:var(--card-cream);font-family:var(--serif);color:var(--ink-navy)}
  .card-back .brand{position:absolute;right:10px;top:12px;color:var(--navy);gap:3px;font-size:7px}
  .card-back .brand__dot{width:6px;height:6px}
  .card-back__name{position:absolute;left:25px;top:39px;font-size:6.6px;font-weight:700;letter-spacing:.2px}
  .card-back__role{position:absolute;left:30px;top:48px;font-size:5.2px}
  .card-back__contacts{position:absolute;left:12px;top:70px;font-size:5.4px;list-style:none}
  .card-back__contacts li{display:flex;gap:5px;align-items:flex-start;margin-bottom:2px;line-height:7.3px}
  .card-back__contacts .icon{width:6.5px;height:6.5px;margin-top:.4px}

  /* envelope */
  .envelope{left:99px;top:813px;width:687px;height:286px;background:var(--envelope);overflow:hidden}
  .envelope__band{position:absolute;left:0;top:0;width:100%;height:68px;background:var(--navy)}
  .envelope__band .brand{position:absolute;left:26px;top:25px;font-size:17px}
  .envelope__band .brand__dot{width:13px;height:13px}
  .envelope__band .network{left:462px;width:198px}
  .envelope__watermark{position:absolute;left:555px;top:130px;width:132px;height:156px;
    background:linear-gradient(150deg,rgba(202,222,239,0) 0%,rgba(202,222,239,.7) 60%,rgba(202,222,239,0) 100%)}
  .envelope__window{position:absolute;left:392px;top:120px;width:229px;height:96px;background:#fff;border:.8px solid #555;border-radius:12px}
  .envelope__contacts{position:absolute;left:26px;top:211px;list-style:none;font-family:var(--serif);font-size:10px;color:var(--ink-navy)}
  .envelope__contacts li{display:flex;gap:9px;align-items:flex-start;line-height:13px;margin-bottom:2.5px}
  .envelope__contacts .icon{width:13px;height:13px}
</style>
</head>
<body>

<svg width="0" height="0" style="position:absolute" aria-hidden="true">
  <symbol id="icon-pin" viewBox="0 0 20 20">
    <rect width="20" height="20" rx="5" fill="#0677ba"/>
    <path d="M10 4a4.2 4.2 0 0 0-4.2 4.2c0 3.2 4.2 7.8 4.2 7.8s4.2-4.6 4.2-7.8A4.2 4.2 0 0 0 10 4zm0 5.8a1.6 1.6 0 1 1 0-3.2 1.6 1.6 0 0 1 0 3.2z" fill="#fff"/>
  </symbol>
  <symbol id="icon-phone" viewBox="0 0 20 20">
    <rect width="20" height="20" rx="5" fill="#0677ba"/>
    <path d="M4.5 8c0-1.6 2.4-2.6 5.5-2.6s5.5 1 5.5 2.6v1h-2.4V7.8H6.9V9H4.5zM6.5 10h7l1 4.5h-9z" fill="#fff"/>
    <circle cx="10" cy="12.2" r="1.2" fill="#0677ba"/>
  </symbol>
  <symbol id="icon-mail" viewBox="0 0 20 20">
    <rect width="20" height="20" rx="5" fill="#0677ba"/>
    <path d="M4.5 8.5 10 5l5.5 3.5V15h-11z" fill="#fff"/>
    <path d="M4.5 8.5 10 12l5.5-3.5" fill="none" stroke="#0677ba" stroke-width="1.2"/>
  </symbol>
</svg>

<!-- Letterhead -->
<section class="sheet letterhead">
  <header class="letterhead__band">
    <div class="brand"><span class="brand__dot"></span><span class="brand__name">Tellwick Asset Management</span></div>
    <div class="network" role="img" aria-label="Constellation network decoration"></div>
  </header>

  <div class="watermark" role="img" aria-label="Faint constellation network decoration"></div>

  <div class="recipient">
    <div class="recipient__name">Name Surname</div>
    <div>Senior Manager</div>
    <div>Address goes here. Street, City, Country</div>
    <div>contact@yourmail.com</div>
    <div>000-987-654-321</div>
  </div>
  <div class="letter-date">Date, 00 May, 2024</div>

  <div class="letter-body">
    <p>Lorem ipsum dolor sit amet, consectetur adipisicing elit, sed do eiusmod tempor incididunt ut labore et dolore magna aliqua. Ut enim ad minim veniam, quis nostrud exercitation ullamco laboris nisi ut aliquip ex ea commodo consequat. Duis aute irure dolor in reprehenderit in voluptate velit esse cillum dolore eu fugiat nulla pariatur. Excepteur sint occaecat cupidatat non proident, sunt in culpa qui officia deserunt mollit anim id est laborum. Sed ut perspiciatis unde omnis iste natus error sit voluptatem accusantium doloremque laudantium, totam rem aperiam, eaque ipsa quae ab illo inventore veritatis et quasi architecto beatae vitae dicta sunt explicabo. Nemo enim ipsam voluptatem quia voluptas sit aspernatur aut odit aut fugit, sed quia consequuntur magni dolores eos qui ratione voluptatem sequi nesciunt. Neque porro voluptatem sequi nesciunt. Nemo enim ipsam voluptatem quia voluptas.</p>
    <p>Lorem ipsum dolor sit amet, consectetur adipisicing elit, sed do eiusmod tempor incididunt ut labore et dolore magna aliqua. Ut enim ad minim veniam, quis nostrud exercitation ullamco laboris nisi ut aliquip ex ea commodo consequat. Duis aute irure dolor in reprehenderit in voluptate velit esse cillum dolore eu fugiat nulla pariatur. Excepteur sint occaecat cupidatat non proident, sunt in culpa qui officia deserunt mollit anim id est laborum. Sed ut perspiciatis unde omnis iste natus error sit voluptatem accusantium doloremque laudantium, totam rem aperiam, eaque ipsa quae ab illo inventore veritatis et quasi architecto beatae vitae dicta sunt explicabo. Nemo enim ipsam voluptatem quia voluptas sit aspernatur aut odit aut.</p>
    <p>Lorem ipsum dolor sit amet, consectetur adipisicing elit, sed do eiusmod tempor incididunt ut labore et dolore magna aliqua. Ut enim ad minim veniam, quis nostrud exercitation ullamco laboris nisi ut aliquip ex ea commodo consequat. .</p>
  </div>

  <div class="signature-block">
    <div class="signature" role="img" aria-label="Handwritten signature"></div>
    <div class="signature-block__name">NAME SURNAME</div>
    <div class="signature-block__role">General Manager</div>
  </div>

  <footer class="letter-footer">
    <span class="letter-footer__item"><svg class="icon"><use href="#icon-pin"/></svg>Lorem ipsum dolor sit amet, ipsum</span>
    <span class="letter-footer__item"><svg class="icon"><use href="#icon-phone"/></svg>000 000 000, 000 000</span>
    <span class="letter-footer__item"><svg class="icon"><use href="#icon-mail"/></svg>infor@tellwickassetmanagement.com</span>
  </footer>
</section>

<!-- Business card front -->
<section class="sheet card-front">
  <div class="network" role="img" aria-label="Constellation network decoration"></div>
  <div class="brand"><span class="brand__dot"></span><span class="brand__name">Tellwick Asset Management</span></div>
</section>

<!-- Business card back -->
<section class="sheet card-back">
  <div class="brand"><span class="brand__dot"></span><span class="brand__name">Tellwick Asset Management</span></div>
  <div class="card-back__name">LOREM IPSUM</div>
  <div class="card-back__role">General Manager</div>
  <ul class="card-back__contacts">
    <li><svg class="icon"><use href="#icon-pin"/></svg><span>Lorem ipsum dolor sit amet, ipsum<br>Lorem ipsum dolor sit - 000 000</span></li>
    <li><svg class="icon"><use href="#icon-phone"/></svg><span>000 000 000, 000 000 0000</span></li>
    <li><svg class="icon"><use href="#icon-mail"/></svg><span>infor@tellwickassetmanagement.com</span></li>
  </ul>
</section>

<!-- Envelope -->
<section class="sheet envelope">
  <header class="envelope__band">
    <div class="brand"><span class="brand__dot"></span><span class="brand__name">Tellwick Asset Management</span></div>
    <div class="network" role="img" aria-label="Constellation network decoration"></div>
  </header>
  <div class="envelope__watermark" role="img" aria-label="Faint constellation network decoration"></div>
  <div class="envelope__window"></div>
  <ul class="envelope__contacts">
    <li><svg class="icon"><use href="#icon-pin"/></svg><span>Lorem ipsum dolor sit amet, ipsum<br>Lorem ipsum dolor sit - 000 000</span></li>
    <li><svg class="icon"><use href="#icon-phone"/></svg><span>000 000 000, 000 000 0000</span></li>
    <li><svg class="icon"><use href="#icon-mail"/></svg><span>infor@tellwickassetmanagement.com</span></li>
  </ul>
</section>

</body>
</html>
```